movie poster for a bittersweet romantic drama

Hello everyone. Looking for a dynamic poster for feature film 'Mabel's Harbor' a romantic drama. It is a bittersweet love story so not rosey lovie dovie type.

300dpi

Please visit the link below for the poster image
https://www.filevault-example.net/s/k8p2r41xqz7mv5b/_Q7T4416.tif?dl=0

poster should have:
1. title of film : Mabel's Harbor
2. tagline of film:
Death knows no names
Love does not know race

3. A film by Lucinda P. Okwemba
4 Include the logo for 'Teruvo Films' attached below

poster size:
1. 8x10
2. thumnail
3. landscape with just film title
4. 27 by 41

Target Market(s)

15-55 men and mostly women

Industry/Entity Type

Film Production

Colors

Designer to choose colors to be used in the design.

Requirements
Must have
• Dynamic and vibrant
• it is a romantic drama so love on a serious note
Nice to have
• Play with romantic fonts but don't overdo it.
Should not have
• must not look like a romance novel

```html
<!DOCTYPE html>
<html lang="en">
<head>
<meta charset="utf-8">
<title>Mabel's Harbor — Poster</title>
<link rel="stylesheet" href="https://fonts.googleapis.com/css2?family=Libre+Caslon+Display&family=Open+Sans:wght@700&display=swap">
<style>
  :root {
    --sky-top: #5aa8e9;
    --sky-mid: #9ac8f2;
    --sky-bottom: #5ea5e6;
    --hill: #5f8272;
    --hill-deep: #476b5d;
    --ochre: #d08a4a;
    --meadow-yellow: #cfd12e;
    --meadow-green: #3f9a35;
    --scrub: #3c5a2c;
    --ink-white: #ffffff;
    --logo-ink: #1f3f7a;
  }
  html, body {
    margin: 0;
    padding: 0;
    width: 960px;
    height: 1200px;
    overflow: hidden;
  }
  .poster {
    position: relative;
    width: 960px;
    height: 1200px;
    overflow: hidden;
    background: linear-gradient(180deg,
      var(--sky-top) 0%,
      #5eaaea 18%,
      var(--sky-mid) 48%,
      #8fc1f0 78%,
      var(--sky-bottom) 100%);
  }
  .tagline {
    position: absolute;
    top: 52px;
    left: 0;
    width: 100%;
    margin: 0;
    text-align: center;
    font-family: 'Libre Caslon Display', serif;
    font-size: 19px;
    line-height: 25px;
    letter-spacing: 0.2px;
    color: var(--ink-white);
  }
  .landscape {
    position: absolute;
    top: 246px;
    left: 0;
    width: 960px;
    height: 722px;
    background: linear-gradient(180deg,
      #6c9287 0%,
      var(--hill) 6%,
      var(--hill-deep) 14%,
      #58786a 19%,
      var(--ochre) 24%,
      var(--meadow-yellow) 29%,
      var(--meadow-green) 35%,
      #b6c92c 41%,
      var(--scrub) 49%,
      #2f4a26 51%,
      #b6c92c 60%,
      var(--meadow-green) 66%,
      var(--meadow-yellow) 71%,
      var(--ochre) 76%,
      #58786a 81%,
      var(--hill-deep) 87%,
      var(--hill) 94%,
      #6c9287 100%);
  }
  .title-block {
    position: absolute;
    top: 462px;
    left: 0;
    width: 960px;
    text-align: center;
  }
  .title {
    margin: 0;
    font-family: 'Libre Caslon Display', serif;
    font-weight: 400;
    font-size: 132px;
    line-height: 116px;
    letter-spacing: -1px;
    color: var(--ink-white);
    text-transform: uppercase;
  }
  .credit {
    position: absolute;
    top: 706px;
    right: 256px;
    margin: 0;
    font-family: 'Open Sans', sans-serif;
    font-weight: 700;
    font-size: 15px;
    letter-spacing: 1px;
    color: var(--ink-white);
    text-transform: uppercase;
  }
  .studio {
    position: absolute;
    right: 30px;
    bottom: 34px;
    display: flex;
    align-items: center;
    gap: 8px;
  }
  .studio-mark {
    width: 14px;
    height: 14px;
    background: var(--logo-ink);
  }
  .studio-name {
    font-family: 'Open Sans', sans-serif;
    font-weight: 700;
    font-size: 14px;
    letter-spacing: 1px;
    color: var(--logo-ink);
    text-transform: uppercase;
  }
</style>
</head>
<body>
  <main class="poster">
    <p class="tagline">DEATH KNOWS NO NAMES<br>LOVE DOES NOT KNOW RACE</p>

    <div class="landscape" role="img" aria-label="Mirrored photograph of a wildflower-covered valley with green fields, yellow and orange blooms and rocky hills reflected below"></div>

    <div class="title-block">
      <h1 class="title">Mabel’s<br>Harbor</h1>
    </div>
    <p class="credit">A film by Lucinda P. Okwemba</p>

    <div class="studio">
      <span class="studio-mark"></span>
      <span class="studio-name">Teruvo Films</span>
    </div>
  </main>
</body>
</html>
```